Startup Drone Platform Company business card

We are needing a business card design for our employees. We are a startup drone platform. We are looking for a business card that has our logo on one side, with the employee/company details on the opposite side. We are looking for something that is very eye catching, modern, and bold.

Target Market(s)

This will target both drone pilots and drone businesses, along with all the industries that could utilize drone services (aerial video, aerial photos, inspections, 3d mapping, etc).

Industry/Entity Type

Business

```html
<!DOCTYPE html>
<html lang="en">
<head>
<meta charset="utf-8">
<title>Skyward Rentals – Business Card</title>
<link rel="stylesheet" href="https://fonts.googleapis.com/css2?family=Open+Sans:wght@400;600&display=swap">
<style>
  :root {
    --page: #d8d3cb;
    --ink: #070808;
    --teal: #3fbccb;
    --white: #ffffff;
    --frost-light: #eef0ef;
    --frost-dark: #d3d7d7;
    --brand-ink: #121414;
  }
  * { box-sizing: border-box; margin: 0; padding: 0; }
  html, body {
    width: 1200px; height: 902px; overflow: hidden;
    background: var(--page);
    font-family: "Open Sans", Arial, sans-serif;
  }
  .business-card {
    position: absolute; left: 100px; top: 166px;
    width: 1000px; height: 569px;
    background: linear-gradient(160deg, var(--frost-light), var(--frost-dark));
    box-shadow: 0 10px 30px rgba(0,0,0,0.18);
    overflow: hidden;
  }
  .card-shapes { position: absolute; inset: 0; }
  .accent-bar {
    position: absolute; left: 0; top: 103px;
    width: 21px; height: 60px; background: var(--teal);
  }
  .person { position: absolute; left: 56px; top: 96px; color: var(--white); }
  .person-name { font-size: 35px; font-weight: 600; line-height: 1.1; white-space: nowrap; }
  .person-title { font-size: 26px; font-weight: 400; color: var(--teal); line-height: 1.05; }
  .address {
    position: absolute; left: 59px; top: 295px;
    color: var(--white); font-size: 26px; line-height: 33px;
    font-style: normal; white-space: nowrap;
  }
  .contacts {
    position: absolute; left: 59px; top: 386px;
    list-style: none; color: var(--white); font-size: 26px; white-space: nowrap;
  }
  .contacts li { display: flex; align-items: center; height: 33px; }
  .contact-icon { width: 25px; height: 25px; margin-right: 14px; flex: none; }
  .brand {
    position: absolute; left: 566px; width: 400px; top: 398px;
    text-align: center; font-size: 30px; font-weight: 400;
    letter-spacing: 0.2em; color: var(--brand-ink); white-space: nowrap;
  }
</style>
</head>
<body>
<main class="business-card">
  <svg class="card-shapes" width="1000" height="569" viewBox="0 0 1000 569">
    <polygon points="0,0 357,0 564,569 0,569" fill="var(--ink)"/>
    <polygon points="356,0 417,0 565,569 543,569" fill="var(--teal)"/>
    <polygon points="417,0 422,0 570,569 565,569" fill="var(--white)"/>
  </svg>

  <div class="accent-bar"></div>
  <header class="person">
    <h1 class="person-name">Employee Name</h1>
    <p class="person-title">Director</p>
  </header>

  <address class="address">
    Skyward Rentals Inc<br>Maple Ave, Brookfield 00000
  </address>

  <ul class="contacts">
    <li>
      <svg class="contact-icon" viewBox="0 0 25 25" aria-hidden="true">
        <rect width="25" height="25" fill="var(--teal)"/>
        <path d="M6 9 Q12.5 4 19 9 L17 11 L15 9.5 L10 9.5 L8 11 Z M8 12 H17 L18 19 H7 Z" fill="var(--ink)"/>
      </svg>
      0100 555 012
    </li>
    <li>
      <svg class="contact-icon" viewBox="0 0 25 25" aria-hidden="true">
        <rect width="25" height="25" fill="var(--teal)"/>
        <rect x="5" y="7" width="15" height="11" fill="none" stroke="var(--ink)" stroke-width="1.6"/>
        <path d="M5 7 L12.5 13 L20 7 M5 18 L10.5 12 M20 18 L14.5 12" fill="none" stroke="var(--ink)" stroke-width="1.4"/>
      </svg>
      info@skywardhire.com
    </li>
    <li>
      <svg class="contact-icon" viewBox="0 0 25 25" aria-hidden="true">
        <rect width="25" height="25" fill="var(--teal)"/>
        <circle cx="12.5" cy="12.5" r="7" fill="none" stroke="var(--ink)" stroke-width="1.5"/>
        <ellipse cx="12.5" cy="12.5" rx="3" ry="7" fill="none" stroke="var(--ink)" stroke-width="1.2"/>
        <path d="M5.5 12.5 H19.5 M7 9 H18 M7 16 H18" stroke="var(--ink)" stroke-width="1.2"/>
      </svg>
      www.skywardhire.com
    </li>
  </ul>

  <p class="brand">SKYWARD RENTALS</p>
</main>
</body>
</html>
```